German tourism publishing house needs for international wellness hotel guide

We are planning as a print catalog. For this hotel directory we need a meaningful and appealing cover. The contents, a wide offer of wellness hotels should be recognizable at first sight. The title should make you want to go on a wellness holiday. The target group of the book are customers. We are looking forward to your next visit! The title "Wellness Hotels" should be larger on the cover written. The "Bravora logo" should be smaller on the cover. Please integrate the Internet address www.bravora-example.de small on the cover

Industry/Entity Type

Tourism

Font styles to use
Serif
Sans Serif

Colors
0355a3
ffffff
85acd3

Requirements
Must have
• We are looking forward to your next visit! The title "Wellness Hotels" should be larger on the cover written. The "Bravora logo" should be smaller on the cover.
Nice to have
• Please integrate the Internet address www.bravora-example.de small on the cover

```html
<!DOCTYPE html>
<html lang="en">
<head>
<meta charset="utf-8">
<title>Wellness Hotels – Cover</title>
<link rel="stylesheet" href="https://fonts.googleapis.com/css2?family=Cinzel:wght@400;600&family=Montserrat:wght@600&display=swap">
<style>
  :root {
    --brand-blue: #0355a3;
    --brand-blue-light: #85acd3;
    --logo-blue: #1f5fb0;
    --white: #ffffff;
    --stage: #8e8b8c;
    --night: #1c1a1a;
  }
  * { box-sizing: border-box; margin: 0; padding: 0; }
  html, body { width: 1200px; height: 1200px; overflow: hidden; }
  body { background: var(--stage); position: relative; }

  .cover {
    position: absolute;
    left: 220px; top: 60px;
    width: 760px; height: 1080px;
    background: var(--white);
    padding: 8px;
  }
  .cover-inner {
    position: relative;
    width: 100%; height: 100%;
    overflow: hidden;
    background: var(--night);
  }
  .cover-photo, .leaf-gallery { position: absolute; left: 0; top: 0; width: 100%; height: 100%; }

  .brand-name {
    position: absolute;
    left: 0; right: 0; top: 32px;
    text-align: center;
    font-family: "Cinzel", serif;
    font-weight: 400;
    font-size: 32px;
    line-height: 1;
    color: var(--logo-blue);
    letter-spacing: 1px;
  }

  .title {
    font-family: "Cinzel", serif;
    font-weight: 600;
    color: var(--white);
    line-height: 1;
  }
  .title-line { position: absolute; white-space: nowrap; }
  .title-line.wellness { left: 58px; top: 92px; }
  .title-line.hotels { left: 272px; top: 174px; }
  .initial { font-size: 118px; }
  .rest { font-size: 72px; letter-spacing: 14px; }

  .url-band {
    position: absolute;
    left: 0; right: 0; bottom: 0;
    height: 32px;
    background: var(--brand-blue);
    display: flex; align-items: center; justify-content: center;
    font-family: "Montserrat", sans-serif;
    font-weight: 600;
    font-size: 19px;
    color: var(--white);
    letter-spacing: 1.5px;
  }
</style>
</head>
<body>
  <div class="cover">
    <div class="cover-inner">
      <svg class="cover-photo" viewBox="0 0 744 1064" role="img" aria-label="Blurred spa still life: rolled towels, lit tealight candles on wood and a purple tulip">
        <defs>
          <radialGradient id="glow" cx="0.62" cy="0.72" r="0.6">
            <stop offset="0" stop-color="#f7c66a"/>
            <stop offset="0.45" stop-color="#b07a3c"/>
            <stop offset="1" stop-color="#1c1a1a" stop-opacity="0"/>
          </radialGradient>
          <linearGradient id="dusk" x1="0" y1="0" x2="0" y2="1">
            <stop offset="0" stop-color="#1c1a1a"/>
            <stop offset="0.35" stop-color="#2a2624"/>
            <stop offset="0.7" stop-color="#6b4a2c"/>
            <stop offset="1" stop-color="#8a5a34"/>
          </linearGradient>
        </defs>
        <rect width="744" height="1064" fill="url(#dusk)"/>
        <rect width="744" height="1064" fill="url(#glow)"/>
      </svg>

      <svg class="leaf-gallery" viewBox="0 0 744 1064">
        <defs>
          <linearGradient id="sauna" x1="0" y1="0" x2="0" y2="1">
            <stop offset="0" stop-color="#e3a06a"/>
            <stop offset="0.35" stop-color="#c4703a"/>
            <stop offset="0.65" stop-color="#9a5128"/>
            <stop offset="0.85" stop-color="#d8b7a8"/>
            <stop offset="1" stop-color="#b9a3c4"/>
          </linearGradient>
          <linearGradient id="pool" x1="0" y1="0" x2="0" y2="1">
            <stop offset="0" stop-color="#a8692e"/>
            <stop offset="0.3" stop-color="#d9a258"/>
            <stop offset="0.55" stop-color="#f0d59c"/>
            <stop offset="0.72" stop-color="#5fc7d4"/>
            <stop offset="1" stop-color="#2f9fb4"/>
          </linearGradient>
          <linearGradient id="steam" x1="0" y1="0" x2="1" y2="0">
            <stop offset="0" stop-color="#f0b25a"/>
            <stop offset="0.3" stop-color="#a5713f"/>
            <stop offset="0.55" stop-color="#6e5039"/>
            <stop offset="1" stop-color="#b8b2a8"/>
          </linearGradient>
        </defs>
        <path role="img" aria-label="Hotel sauna interior with warm wooden walls and benches" d="M-10,415 C0,330 40,310 120,295 C220,280 300,276 358,272 C310,310 270,400 220,470 C180,520 90,536 -10,540 Z" fill="url(#sauna)" stroke="#ffffff" stroke-width="4"/>
        <path role="img" aria-label="Indoor hotel swimming pool under a wooden ceiling" d="M-10,650 C0,580 50,555 130,545 C230,532 300,528 358,524 C310,565 270,645 220,705 C180,755 90,770 -10,775 Z" fill="url(#pool)" stroke="#ffffff" stroke-width="4"/>
        <path role="img" aria-label="Spa relaxation area with a foot bath and sauna doors" d="M-10,885 C0,815 50,790 130,780 C230,768 300,764 358,760 C310,800 270,880 220,940 C180,990 90,1005 -10,1010 Z" fill="url(#steam)" stroke="#ffffff" stroke-width="4"/>
      </svg>

      <div class="brand-name">Bravora</div>

      <h1 class="title">
        <span class="title-line wellness"><span class="initial">W</span><span class="rest">ELLNESS</span></span>
        <span class="title-line hotels"><span class="initial">H</span><span class="rest">OTELS</span></span>
      </h1>

      <div class="url-band">www.bravora-example.de</div>
    </div>
  </div>
</body>
</html>
```